Website for an interior designer

We need a new website for Clara Beth Holloway whose new business name is Clara Beth Holloway Interiors. She is a residential interior designer with a mix of modern and contemporary tastes. We are in the process of overhauling her website which is +15 years old and not an accurate reflection of her tastes. The uploaded photos are from some of the houses she has done as well as her logo(s). We would need a section for "About Us" that would have a paragraph of text and bullets showing services and a gallery for photos (~12 total, more to come). A contract page would be optional. The client likes the feel/look of this website: https://www.pondrickstudio.example/ but doesn't want to copy it exactly.

Target Market(s)

Upscale home owners

Industry/Entity Type

Interior Design

Coding

Coded - Design and coding required

Number of Pages Required

4 page

Colors

Designer to choose only greyscale colors for use in the design.

Requirements
Must have
• Home page, about us page, gallery page, contact us page.

```html
<!DOCTYPE html>
<html lang="en">
<head>
<meta charset="utf-8">
<title>Clara Beth Holloway Interiors</title>
<link href="https://fonts.googleapis.com/css2?family=Montserrat:wght@400;500;600;700&family=Open+Sans:wght@400;600&display=swap" rel="stylesheet">
<style>
:root{
  --accent:#3a3a3a;
  --accent-strong:#1f1f1f;
  --accent-light:#e9e9e9;
  --ink:#2b2b2b;
  --text:#6d6d6d;
  --muted:#9a9a9a;
  --line:#e3e3e3;
  --paper:#ffffff;
  --soft:#f5f5f5;
  --dark:#1e1f21;
}
*{box-sizing:border-box;margin:0;padding:0}
html,body{width:1200px;height:3140px;overflow:hidden;background:var(--paper)}
body{font-family:"Open Sans",Arial,sans-serif;color:var(--text);font-size:12px;line-height:1.7}
.page{position:relative;width:1200px;height:3140px}

/* nav */
.site-nav{position:absolute;top:0;left:0;width:1200px;height:58px;background:rgba(255,255,255,.96);display:flex;align-items:center;justify-content:center;z-index:3;font-family:"Montserrat",Arial,sans-serif;font-size:10px;font-weight:600;letter-spacing:.5px;color:var(--ink)}
.nav-group{display:flex;gap:34px;width:340px}
.nav-group.left{justify-content:flex-end}
.nav-group a{color:var(--ink);text-decoration:none}
.nav-group a.active{color:var(--accent-strong);border-top:2px solid var(--accent-strong);padding-top:4px}
.brand{width:220px;text-align:center;font-family:"Montserrat",sans-serif;color:var(--ink)}
.brand-mark{display:block;width:22px;height:22px;margin:0 auto 2px;border:1px solid var(--ink);border-radius:50%}
.brand-name{font-size:8px;letter-spacing:2px;font-weight:500;line-height:1.3}
.search-icon{position:absolute;right:130px;top:22px}

/* hero */
.hero{position:absolute;top:0;left:0;width:1200px;height:580px;overflow:hidden}
.hero-photo{position:absolute;inset:0;background:linear-gradient(180deg,#555555 0%,#7f7f7f 45%,#c8c8c8 85%,#e2e2e2 100%)}
.hero-shade{position:absolute;inset:0;background:rgba(30,30,30,.35)}
.hero-copy{position:absolute;top:225px;left:0;width:1200px;text-align:center}
.hero-title{font-family:"Montserrat",sans-serif;font-weight:700;font-size:34px;line-height:1.15;letter-spacing:2px;color:#ffffff;text-transform:uppercase}
.hero-sub{color:#f0f0f0;font-size:11px;margin:10px auto 16px;width:520px;line-height:1.5}
.btn{display:inline-block;font-family:"Montserrat",sans-serif;font-size:10px;font-weight:600;padding:8px 18px;border-radius:2px}
.btn-solid{background:var(--accent-strong);color:#fff}
.btn-outline{border:1px solid #cfcfcf;color:var(--muted);background:#fff}
.hero-edge{position:absolute;bottom:0;left:0}

/* section heads */
.eyebrow{font-family:"Montserrat",sans-serif;font-size:8px;letter-spacing:1px;color:var(--muted);text-align:center}
.section-title{font-family:"Montserrat",sans-serif;font-size:15px;font-weight:700;letter-spacing:1px;text-align:center;color:var(--ink);text-transform:uppercase}
.section-title::after{content:"";display:block;width:34px;height:2px;background:var(--accent);margin:8px auto 0}
.on-dark .section-title{color:#fff}
.on-dark .section-title::after{background:#cfcfcf}
.on-dark .eyebrow,.on-dark .section-lead{color:#d6d6d6}
.section-lead{font-size:11px;text-align:center;width:720px;margin:12px auto 0;line-height:1.6}

/* about */
.about{position:absolute;top:590px;left:0;width:1200px;height:420px}
.about-body{position:absolute;top:70px;left:172px;width:500px}
.about-intro{color:var(--accent);font-size:14px;line-height:1.5;margin-bottom:12px}
.about-body p{margin-bottom:10px}
.about-body .btn{margin-top:10px}
.about-figure{position:absolute;top:70px;left:716px;width:310px;height:300px}
.about-frame{position:absolute;top:12px;left:14px;width:310px;height:300px;border:1px solid var(--line)}
.about-photo{position:absolute;inset:0;background:linear-gradient(135deg,#4d4d4d,#9c9c9c 55%,#dadada)}

/* services */
.services{position:absolute;top:1040px;left:0;width:1200px;height:500px;background:linear-gradient(180deg,#2a2a2a,#4a4a4a 60%,#3a3a3a)}
.services .section-head{padding-top:50px}
.service-cards{position:absolute;top:150px;left:172px;display:flex;gap:16px}
.service-card{width:280px;height:236px;background:#fff;text-align:center;padding:28px 26px 0}
.service-card h3{font-family:"Montserrat",sans-serif;font-size:11px;font-weight:700;color:var(--accent-strong);margin:12px 0 8px;text-transform:uppercase}
.service-card p{font-size:10px;line-height:1.6;margin-bottom:14px}
.service-card .btn{padding:5px 12px;font-size:9px}
.view-all{position:absolute;top:410px;width:1200px;text-align:center;font-family:"Montserrat",sans-serif;font-size:9px;font-weight:600;color:#fff;letter-spacing:1px}

/* gallery */
.gallery{position:absolute;top:1560px;left:0;width:1200px;height:500px}
.gallery-grid{position:absolute;top:100px;left:172px;width:856px;height:342px;display:grid;grid-template-columns:272px 272px 272px;grid-template-rows:163px 163px;gap:16px 20px}
.tile{position:relative}
.tile.tall{grid-row:1 / span 2;grid-column:2}
.tile-a{background:linear-gradient(135deg,#a5a5a5,#e2e2e2)}
.tile-b{background:linear-gradient(135deg,#7b7b7b,#d1d1d1)}
.tile-c{background:linear-gradient(180deg,#4b4b4b,#8a8a8a)}
.tile-d{background:linear-gradient(135deg,#cfcfcf,#f1f1f1)}
.tile-e{background:linear-gradient(135deg,#bbbbbb,#eeeeee)}
.tile-label{position:absolute;top:150px;left:0;width:100%;text-align:center;color:#fff;font-family:"Montserrat",sans-serif;font-size:11px;font-weight:600;letter-spacing:1px}
.tile-label small{display:block;font-size:8px;font-weight:400;opacity:.85}
.gallery .btn{position:absolute;top:464px;left:546px}

/* blog */
.blog{position:absolute;top:2080px;left:0;width:1200px;height:480px;background:linear-gradient(180deg,#1d1d1d,#3a3a3a 55%,#262626)}
.blog .section-head{padding-top:36px}
.blog-cards{position:absolute;top:130px;left:172px;display:flex;gap:16px}
.post{width:280px;height:260px;background:#fff}
.post-photo{height:120px}
.post-body{padding:10px 14px}
.post h3{font-family:"Montserrat",sans-serif;font-size:11px;font-weight:600;color:var(--ink)}
.post-meta{font-size:8px;color:var(--muted);display:flex;gap:12px;align-items:center;margin:2px 0 6px}
.post p{font-size:9px;line-height:1.6}
.post-foot{display:flex;justify-content:space-between;border-top:1px solid var(--line);margin-top:8px;padding-top:6px;font-size:9px}
.post-foot .more{color:var(--accent-strong);font-weight:600}
.blog .btn{position:absolute;top:418px;left:550px}

/* follow */
.follow{position:absolute;top:2590px;left:0;width:1200px;height:230px;text-align:center}
.follow-dot{width:26px;height:26px;border:2px solid var(--ink);border-radius:50%;margin:0 auto 8px}
.follow-title{font-family:"Montserrat",sans-serif;font-size:12px;font-weight:600;color:var(--ink)}
.feed{position:absolute;top:70px;left:172px;display:flex;gap:8px}
.feed div{width:165px;height:130px}

/* footer */
.site-footer{position:absolute;top:2830px;left:0;width:1200px;height:310px;border-top:1px solid var(--line);text-align:center}
.footer-brand{margin:20px auto 0}
.footer-links{display:flex;justify-content:center;gap:14px;font-family:"Montserrat",sans-serif;font-size:9px;font-weight:600;color:var(--ink);margin:18px 0 20px}
.footer-links span.sep{color:var(--line)}
.footer-contacts{display:flex;justify-content:center;gap:60px;font-size:9px;line-height:1.5}
.footer-contacts div{width:120px}
.footer-contacts svg{display:block;margin:0 auto 4px}
.footer-meta{display:flex;justify-content:center;gap:20px;align-items:center;border-top:1px solid var(--line);border-bottom:1px solid var(--line);width:620px;margin:18px auto 0;padding:8px 0;font-size:9px}
.socials{display:flex;gap:8px}
.socials span{width:14px;height:14px;border-radius:50%;background:var(--ink);display:block}
.copyright{font-size:9px;color:var(--muted);margin-top:14px}
</style>
</head>
<body>
<div class="page">

  <section class="hero">
    <div class="hero-photo" role="img" aria-label="Bright entry hall with lanterns, open doorway and warm wood floor"></div>
    <div class="hero-shade"></div>
    <div class="hero-copy">
      <h1 class="hero-title">Clara Beth Holloway<br>Homes for all interiors</h1>
      <p class="hero-sub">Warm modern rooms shaped around the way you live, from first sketch to the final styled detail.</p>
      <span class="btn btn-solid">VIEW MORE</span>
    </div>
    <svg class="hero-edge" width="1200" height="40" viewBox="0 0 1200 40"><polygon points="0,40 0,20 600,38 1200,0 1200,40" fill="#fff"/></svg>
  </section>

  <header class="site-nav">
    <nav class="nav-group left"><a class="active">HOME</a><a>OUR STORY</a><a>SERVICES</a></nav>
    <div class="brand"><span class="brand-mark"></span><div class="brand-name">CLARA BETH HOLLOWAY<br>INTERIORS</div></div>
    <nav class="nav-group"><a>GALLERY</a><a>BLOG</a><a>CONTACT US</a></nav>
    <svg class="search-icon" width="12" height="12" viewBox="0 0 12 12"><circle cx="5" cy="5" r="4" fill="none" stroke="#2b2b2b" stroke-width="1.5"/><line x1="8" y1="8" x2="11.5" y2="11.5" stroke="#2b2b2b" stroke-width="1.5"/></svg>
  </header>

  <section class="about">
    <p class="eyebrow">WHO WE ARE</p>
    <h2 class="section-title">Clara Beth Holloway</h2>
    <div class="about-body">
      <p class="about-intro">Calm, layered homes with a modern and contemporary spirit, crafted for families who value comfort, quality and lasting style.</p>
      <p>Clara Beth Holloway has shaped private residences for more than fifteen years, guiding each client from the first walk-through to the final placement of art. Her work balances clean lines with soft texture and a restrained greyscale palette.</p>
      <p>Every project begins with listening. We study how you move through your home, where light falls through the day and which pieces already hold meaning, then build a plan that feels personal.</p>
      <p>From furniture selection to custom millwork, our studio manages sourcing, trades and installation so the finished rooms arrive ready to live in.</p>
      <span class="btn btn-outline">Read More Story</span>
    </div>
    <div class="about-figure">
      <div class="about-frame"></div>
      <div class="about-photo" role="img" aria-label="Living room with grey sofas, glass coffee table and tall windows"></div>
    </div>
  </section>

  <section class="services on-dark">
    <div class="section-head">
      <p class="eyebrow">WHAT WE DO</p>
      <h2 class="section-title">Our Service</h2>
      <p class="section-lead">Full service design for upscale homes, from single rooms to complete renovations, delivered with care at every step.</p>
    </div>
    <div class="service-cards">
      <div class="service-card">
        <svg width="40" height="30" viewBox="0 0 40 30"><rect x="4" y="10" width="32" height="12" rx="3" fill="none" stroke="#3a3a3a" stroke-width="2"/><line x1="8" y1="22" x2="8" y2="28" stroke="#3a3a3a" stroke-width="2"/><line x1="32" y1="22" x2="32" y2="28" stroke="#3a3a3a" stroke-width="2"/></svg>
        <h3>Furniture Interior</h3>
        <p>Curated pieces and custom items chosen for scale, comfort and a finish that lasts for years.</p>
        <span class="btn btn-outline">Read More</span>
      </div>
      <div class="service-card">
        <svg width="40" height="30" viewBox="0 0 40 30"><rect x="6" y="3" width="28" height="22" fill="none" stroke="#3a3a3a" stroke-width="2"/><polyline points="9,21 17,12 23,18 27,14 31,21" fill="none" stroke="#3a3a3a" stroke-width="2"/></svg>
        <h3>Home Art Interior</h3>
        <p>Art sourcing and placement that gives each room a focal point and a clear sense of character.</p>
        <span class="btn btn-outline">Read More</span>
      </div>
      <div class="service-card">
        <svg width="40" height="30" viewBox="0 0 40 30"><polygon points="12,4 28,4 32,14 8,14" fill="none" stroke="#3a3a3a" stroke-width="2"/><line x1="20" y1="14" x2="20" y2="26" stroke="#3a3a3a" stroke-width="2"/><line x1="13" y1="27" x2="27" y2="27" stroke="#3a3a3a" stroke-width="2"/></svg>
        <h3>Home Decor Interior</h3>
        <p>Lighting, textiles and finishing touches that pull a space together into one calm story.</p>
        <span class="btn btn-outline">Read More</span>
      </div>
    </div>
    <p class="view-all">VIEW ALL</p>
  </section>

  <section class="gallery">
    <p class="eyebrow">OUR WORK</p>
    <h2 class="section-title">Our Gallery</h2>
    <p class="section-lead">A selection of recent residences across living rooms, kitchens and quiet private spaces.</p>
    <div class="gallery-grid">
      <div class="tile tile-a" role="img" aria-label="Sitting room with neutral armchairs"></div>
      <div class="tile tall tile-c" role="img" aria-label="Dark hallway opening to a lit dining room"><p class="tile-label">INTERIOR DESIGN<small>Residence</small></p></div>
      <div class="tile tile-d" role="img" aria-label="White kitchen with island and pendant lights"></div>
      <div class="tile tile-b" role="img" aria-label="Staircase with slim railing"></div>
      <div class="tile tile-e" role="img" aria-label="Living room with white sofas"></div>
    </div>
    <span class="btn btn-outline">View More Gallery</span>
  </section>

  <section class="blog on-dark">
    <div class="section-head">
      <p class="eyebrow">FROM THE STUDIO</p>
      <h2 class="section-title">Latest Blog</h2>
      <p class="section-lead">Notes on materials, planning and the small choices that make a home feel finished.</p>
    </div>
    <div class="blog-cards">
      <article class="post">
        <div class="post-photo" role="img" aria-label="Bright hallway with white walls" style="background:linear-gradient(135deg,#bdbdbd,#f2f2f2)"></div>
        <div class="post-body">
          <h3>Interior Design for Hall</h3>
          <div class="post-meta"><span>● Admin</span><span>● Jun 12, 2024</span></div>
          <p>How to plan an entry hall that welcomes guests and still works for busy family mornings.</p>
          <div class="post-foot"><span class="more">Read More »</span><span>0 Comments</span></div>
        </div>
      </article>
      <article class="post">
        <div class="post-photo" role="img" aria-label="Room with framed art and soft seating" style="background:linear-gradient(135deg,#8c8c8c,#dadada)"></div>
        <div class="post-body">
          <h3>Interior Design for Art &amp; Craft</h3>
          <div class="post-meta"><span>● Admin</span><span>● Jun 05, 2024</span></div>
          <p>Choosing frames, heights and lighting so every piece of art earns its place on the wall.</p>
          <div class="post-foot"><span class="more">Read More »</span><span>0 Comments</span></div>
        </div>
      </article>
      <article class="post">
        <div class="post-photo" role="img" aria-label="Living room with cream sofa and round table" style="background:linear-gradient(135deg,#c4c4c4,#f1f1f1)"></div>
        <div class="post-body">
          <h3>Living Room Interior Design</h3>
          <div class="post-meta"><span>● Admin</span><span>● May 28, 2024</span></div>
          <p>Layering texture in a quiet palette so a living room feels warm without feeling busy.</p>
          <div class="post-foot"><span class="more">Read More »</span><span>0 Comments</span></div>
        </div>
      </article>
    </div>
    <span class="btn btn-outline">View More Blog</span>
  </section>

  <section class="follow">
    <div class="follow-dot"></div>
    <p class="follow-title">Follow by @ Clara Beth Holloway in Snapfolio</p>
    <div class="feed">
      <div role="img" aria-label="Grey living room" style="background:linear-gradient(135deg,#6f6f6f,#bdbdbd)"></div>
      <div role="img" aria-label="Dining table by window" style="background:linear-gradient(135deg,#a5a5a5,#e4e4e4)"></div>
      <div role="img" aria-label="Dark study with shelving" style="background:linear-gradient(135deg,#3d3d3d,#8a8a8a)"></div>
      <div role="img" aria-label="Bright bedroom" style="background:linear-gradient(135deg,#d6d6d6,#f5f5f5)"></div>
      <div role="img" aria-label="Lounge with armchairs" style="background:linear-gradient(135deg,#888888,#d0d0d0)"></div>
    </div>
  </section>

  <footer class="site-footer">
    <div class="brand footer-brand"><span class="brand-mark"></span><div class="brand-name">CLARA BETH HOLLOWAY<br>INTERIORS</div></div>
    <nav class="footer-links"><span>HOME</span><span class="sep">|</span><span>OUR STORY</span><span class="sep">|</span><span>SERVICES</span><span class="sep">|</span><span>GALLERY</span><span class="sep">|</span><span>BLOG</span><span class="sep">|</span><span>CONTACT US</span></nav>
    <div class="footer-contacts">
      <div><svg width="12" height="14" viewBox="0 0 12 14"><path d="M6 13C2 8 1 6 1 5a5 5 0 0 1 10 0c0 1-1 3-5 8z" fill="#6d6d6d"/><circle cx="6" cy="5" r="1.8" fill="#fff"/></svg>48 Linden Row, Suite 2<br>Alder Bay, OR 97000</div>
      <div><svg width="12" height="14" viewBox="0 0 12 14"><path d="M2 1h3l1 3-2 1a7 7 0 0 0 3 4l1-2 3 1v3a1 1 0 0 1-1 1C5 12 0 7 1 2a1 1 0 0 1 1-1z" fill="#6d6d6d"/></svg>+1 (555) 014-2290<br>+1 (555) 014-2291</div>
      <div><svg width="14" height="14" viewBox="0 0 14 14"><circle cx="7" cy="7" r="6" fill="none" stroke="#6d6d6d" stroke-width="1.5"/><polyline points="7,3.5 7,7 9.5,8.5" fill="none" stroke="#6d6d6d" stroke-width="1.5"/></svg>Mon to Sat : 9AM - 6PM<br>Sun : Closed</div>
    </div>
    <div class="footer-meta">
      <span>✉ hello@hollowayinteriors.example</span>
      <div class="socials"><span></span><span></span><span></span></div>
    </div>
    <p class="copyright">Copyright © Holloway Studio. All Rights Reserved.</p>
  </footer>

</div>
</body>
</html>
```